Real Estate Entrepreneur needs a business card

I am a real estate entrepreneur, I buy houses for investment purposes, I act as a real estate agent representing buyers and sellers in residential home transactions, I am a contractor that does a wide range of home repairs and construction. I'd like a design that can stick with me through the years as my business grows and morphs to fit any niche I decide to pursue as markets change.

Target Market(s)

Anyone with interest that may be related to real estate.

Industry/Entity Type

Real Estate

Contact Information for Business Card

A card that stands out and doesn't put me in any one box. My business will evolve over time and I need a card that can stay relevant.

Colors

Designer to choose colors to be used in the design.

Requirements
Must have
• Character
Nice to have
• I'm open
Should not have
• Cliche houses and hammers

```html
<!DOCTYPE html>
<html lang="en">
<head>
<meta charset="utf-8">
<title>Reid Calloway — Business Card</title>
<link rel="stylesheet" href="https://fonts.googleapis.com/css2?family=Roboto:ital,wght@0,700;1,400&family=Open+Sans:wght@400&family=Marcellus&display=swap">
<style>
  :root {
    --page-bg: #1c1d20;
    --card-white: #f7f7f7;
    --brand-blue: #0f4e7c;
    --divider-blue: #1a3f75;
    --text-gray: #6b6b6b;
    --back-blue-light: #07508a;
    --back-blue-dark: #0a1f40;
    --back-lettering: #dcdcdc;
  }
  * { margin: 0; padding: 0; box-sizing: border-box; }
  html, body { width: 1200px; height: 900px; overflow: hidden; }
  body {
    background: var(--page-bg);
    display: flex;
    flex-direction: column;
    align-items: center;
    justify-content: center;
    gap: 34px;
  }
  .card {
    width: 700px;
    height: 400px;
    border-radius: 3px;
    box-shadow: 0 10px 30px rgba(0,0,0,0.45);
    position: relative;
  }
  .card-front {
    background: var(--card-white);
    display: flex;
    align-items: center;
    justify-content: center;
    gap: 22px;
  }
  .identity { text-align: right; }
  .identity-name {
    font-family: "Roboto", sans-serif;
    font-weight: 700;
    font-size: 34px;
    letter-spacing: 0.5px;
    color: var(--brand-blue);
    text-transform: uppercase;
    line-height: 1.05;
  }
  .identity-title {
    font-family: "Roboto", sans-serif;
    font-style: italic;
    font-weight: 400;
    font-size: 19px;
    color: var(--text-gray);
  }
  .divider {
    width: 1.5px;
    height: 84px;
    background: var(--divider-blue);
  }
  .contact-list { list-style: none; }
  .contact-item {
    display: flex;
    align-items: center;
    gap: 10px;
    font-family: "Open Sans", sans-serif;
    font-size: 17px;
    color: var(--text-gray);
    line-height: 1.55;
  }
  .contact-icon { width: 16px; height: 16px; fill: var(--brand-blue); flex: none; }
  .card-back {
    background: radial-gradient(ellipse at 55% 15%, var(--back-blue-light) 0%, #063968 45%, var(--back-blue-dark) 100%);
    display: flex;
    align-items: center;
    justify-content: center;
  }
  .back-name {
    font-family: "Marcellus", serif;
    font-size: 62px;
    letter-spacing: 3px;
    color: var(--back-lettering);
    text-transform: uppercase;
  }
</style>
</head>
<body>
  <section class="card card-front">
    <div class="identity">
      <h1 class="identity-name">Reid Calloway</h1>
      <p class="identity-title">Real Estate Entrepreneur</p>
    </div>
    <div class="divider"></div>
    <ul class="contact-list">
      <li class="contact-item">
        <svg class="contact-icon" viewBox="0 0 24 24"><path d="M6.6 10.8a15.1 15.1 0 0 0 6.6 6.6l2.2-2.2a1 1 0 0 1 1-.25 11.4 11.4 0 0 0 3.6.57 1 1 0 0 1 1 1V20a1 1 0 0 1-1 1A17 17 0 0 1 3 4a1 1 0 0 1 1-1h3.5a1 1 0 0 1 1 1c0 1.25.2 2.45.57 3.6a1 1 0 0 1-.25 1z"/></svg>
        404.555.0147
      </li>
      <li class="contact-item">
        <svg class="contact-icon" viewBox="0 0 24 24"><path d="M2 5h20v14H2z" fill="none"/><path d="M2 6l10 7 10-7v12H2z"/><path d="M2 5h20l-10 7z"/></svg>
        info@reidcalloway.com
      </li>
      <li class="contact-item">
        <svg class="contact-icon" viewBox="0 0 24 24"><circle cx="12" cy="12" r="10"/><path d="M2 12h20M12 2c3 3 3 17 0 20M12 2c-3 3-3 17 0 20" stroke="#f7f7f7" stroke-width="1.4" fill="none"/></svg>
        www.reidcalloway.com
      </li>
    </ul>
  </section>

  <section class="card card-back">
    <p class="back-name">Reid Calloway</p>
  </section>
</body>
</html>
```